Redesign of a Brochure based on an exsiting example for Web download and email marketing

Can you create a professional brochure based on the attached PDF. We need to keep the name, the logo and the content but everything else can be changed . The PDF will primarily be will be used for web download and email marking but it aslo be printed out for a poster design will be appropriate

Target Market(s)

Business to Business

Industry/Entity Type

Marketing

Font styles to use
Serif

Requirements
Must have
• Must have the existing logo ( in the attached document) and contain the same content

```html
<!DOCTYPE html>
<html lang="en">
<head>
<meta charset="utf-8">
<title>Technology Business Management (TBM) Framework</title>
<link rel="stylesheet" href="https://fonts.googleapis.com/css2?family=Tinos:wght@400;700&family=Arimo:wght@700&display=swap">
<style>
  :root {
    --band-blue: #0a7fcf;
    --tab-blue: #29aae6;
    --box-blue: #00adef;
    --pale-panel: #dcf0fb;
    --title-yellow: #f3e61c;
    --ink: #1b1b1b;
    --white: #ffffff;
  }
  * { margin: 0; padding: 0; box-sizing: border-box; }
  html, body { width: 1200px; height: 848px; overflow: hidden; background: var(--white); }
  .page {
    position: relative; width: 1200px; height: 848px; overflow: hidden;
    background: var(--pale-panel);
    font-family: "Tinos", "Times New Roman", serif;
  }
  .top-band {
    position: absolute; left: 0; top: 0; width: 1200px; height: 175px;
    background: var(--band-blue);
  }
  .content-panel { position: absolute; left: 0; top: 155px; width: 1200px; height: 610px; }
  .bottom-band {
    position: absolute; left: 0; top: 760px; width: 1200px; height: 88px;
    background: linear-gradient(90deg, #2f8fd2 0%, #4aa5df 50%, #2f8fd2 100%);
  }
  .title-tab { position: absolute; left: 0; top: 54px; width: 585px; height: 44px; }
  .title-tab h1 {
    position: absolute; left: 35px; top: 8px;
    font-family: "Tinos", serif; font-weight: 400; font-size: 24px;
    color: var(--title-yellow); white-space: nowrap;
  }
  .brand {
    position: absolute; left: 912px; top: 58px; display: flex; align-items: center; gap: 12px;
  }
  .brand-dot { width: 20px; height: 20px; border-radius: 50%; background: var(--white); }
  .brand-name { font-size: 32px; font-weight: 400; color: var(--white); line-height: 1; }
  .hero-visual {
    position: absolute; left: 0; top: 155px; width: 600px; height: 605px;
    background: radial-gradient(circle at 30% 45%, #f4f9fd 0%, #dcebf6 45%, #c3d9ea 80%, #b7d0e4 100%);
  }
  .diagram-card {
    position: absolute; left: 46px; top: 208px; width: 504px; height: 442px;
    background: rgba(255,255,255,0.55);
  }
  .tier {
    position: absolute; height: 44px; background: var(--box-blue);
    color: var(--white); font-family: "Arimo", Arial, sans-serif; font-weight: 700;
    font-size: 16.5px; display: flex; align-items: center; justify-content: center;
  }
  .connectors { position: absolute; left: 0; top: 0; }
  .intro-copy {
    position: absolute; left: 670px; top: 205px; width: 456px;
    font-size: 13.8px; line-height: 17px; color: var(--ink);
  }
  .intro-copy p { margin-bottom: 9px; }
  .photo { position: absolute; top: 462px; height: 250px; }
  .photo-network { left: 670px; width: 143px; background: linear-gradient(160deg, #0d4f9a, #3ab3ee 55%, #0c5ea8); }
  .photo-disc { left: 825px; width: 141px; background: linear-gradient(170deg, #6b3a15, #f0b22a 45%, #c9472e 70%, #5b2d7a); }
  .photo-finance { left: 978px; width: 141px; background: linear-gradient(165deg, #3c47a8, #8390d8 50%, #2a3c8f); }
  .gauge-icon {
    position: absolute; left: 1085px; top: 730px; width: 79px; height: 91px;
    background: var(--box-blue); border: 2px solid var(--white); border-radius: 8px;
  }
</style>
</head>
<body>
<div class="page">
  <div class="top-band"></div>
  <svg class="content-panel" width="1200" height="610" viewBox="0 0 1200 610">
    <polygon points="0,20 40,0 1150,0 1180,18 1200,18 1200,610 0,610" fill="#dcf0fb"/>
  </svg>
  <div class="hero-visual" role="img" aria-label="Soft pale blue abstract backdrop of binary digits and circular technology motifs"></div>
  <div class="bottom-band"></div>

  <div class="title-tab">
    <svg width="585" height="44" viewBox="0 0 585 44"><polygon points="0,0 555,0 585,22 555,44 0,44" fill="#29aae6"/></svg>
    <h1>Technology Business Management (TBM) Framework</h1>
  </div>

  <div class="brand">
    <div class="brand-dot"></div>
    <div class="brand-name">Costaris</div>
  </div>

  <div class="diagram-card"></div>
  <svg class="connectors" width="600" height="848" viewBox="0 0 600 848" stroke="#111" stroke-width="1.4" fill="#111">
    <line x1="160" y1="315" x2="160" y2="284"/><polygon points="156,286 160,277 164,286" stroke="none"/>
    <line x1="430" y1="315" x2="430" y2="284"/><polygon points="426,286 430,277 434,286" stroke="none"/>
    <line x1="298" y1="412" x2="298" y2="398" fill="none"/>
    <polyline points="247,378 247,398 348,398 348,378" fill="none"/>
    <polygon points="243,380 247,371 251,380" stroke="none"/><polygon points="344,380 348,371 352,380" stroke="none"/>
    <line x1="298" y1="495" x2="298" y2="470"/><polygon points="294,472 298,463 302,472" stroke="none"/>
    <line x1="298" y1="551" x2="298" y2="578"/>
  </svg>
  <div class="tier" style="left:63px;top:229px;width:471px">Business Units</div>
  <div class="tier" style="left:63px;top:322px;width:203px">Products</div>
  <div class="tier" style="left:331px;top:322px;width:203px">Services</div>
  <div class="tier" style="left:63px;top:412px;width:471px">Technology Towers</div>
  <div class="tier" style="left:63px;top:499px;width:471px">Cost Pools: Standardised Costs</div>
  <div class="tier" style="left:63px;top:582px;width:471px">Finance Layer: General Ledger Costs</div>

  <div class="intro-copy">
    <p>TBM provides a simple but clear way to describe IT costs and how they build into technology towers, services and applications.</p>
    <p>The next page details the model layers and categories. It splits costs over three broad categories: Build, Manage and Run. In TBM terminology “Run” is IT that supports the existing business while “Build” is equivalent to change the business.</p>
    <p>The TBM model is shown in the diagram opposite. It does not, however, show the projects layer as this is part of the “change - the - business” IT spend and this model focuses mainly on “run-the-business” IT.</p>
    <p>The cost reference point of the model is the General Ledger, meaning there is always a clear reconciliation with corporate financial systems i.e. A single point of truth.</p>
  </div>

  <div class="photo photo-network" role="img" aria-label="Photo of a blue internet data tunnel"></div>
  <div class="photo photo-disc" role="img" aria-label="Photo of a glowing disc with binary digits and spectrum light"></div>
  <div class="photo photo-finance" role="img" aria-label="Photo of banknotes over a financial chart"></div>

  <div class="gauge-icon">
    <svg width="75" height="87" viewBox="0 0 75 87" fill="none" stroke="#111" stroke-width="3">
      <rect x="31" y="14" width="13" height="44" rx="6.5" fill="#fff"/>
      <circle cx="37.5" cy="64" r="11" fill="#fff"/>
      <line x1="37.5" y1="30" x2="37.5" y2="62" stroke-width="5"/>
      <circle cx="37.5" cy="64" r="6" fill="#111" stroke="none"/>
      <g stroke-width="2"><line x1="22" y1="22" x2="29" y2="22"/><line x1="22" y1="30" x2="29" y2="30"/><line x1="22" y1="38" x2="29" y2="38"/><line x1="22" y1="46" x2="29" y2="46"/>
      <line x1="46" y1="22" x2="53" y2="22"/><line x1="46" y1="30" x2="53" y2="30"/><line x1="46" y1="38" x2="53" y2="38"/><line x1="46" y1="46" x2="53" y2="46"/></g>
    </svg>
  </div>
</div>
</body>
</html>
```